Financial Services Business Card Design

We are a financial services company Based in London, offering Short term Funding Solutions for companies, raising anywhere between £20,000 and £25million pounds.

The Card must have a professional look as it is going to be handed out to professionals I.E Solicitors, Accountants, Company directors and Business owners.

See Attached our company Logo

Industry/Entity Type

Business

Contact Information for Business Card

Brett Kolvane
Suite 41
R T House
Hazelbrook Lane
Watford
WD17 4QL

```html
<!DOCTYPE html>
<html lang="en">
<head>
<meta charset="utf-8">
<title>Meridian Capital Bridge – Business Card</title>
<link rel="stylesheet" href="https://fonts.googleapis.com/css2?family=Open+Sans:wght@400;600;700;800&display=swap">
<style>
  :root {
    --page-bg: #e9e6e1;
    --card-white: #ffffff;
    --card-shade: #eef0f2;
    --brand-blue: #1f5fae;
    --blue-light: #3d86cc;
    --blue-dark: #1c5aa6;
    --accent-green: #3aac3a;
    --ink-grey: #3c4148;
    --text-on-blue: #ffffff;
  }
  * { box-sizing: border-box; margin: 0; padding: 0; }
  html, body { width: 1200px; height: 843px; overflow: hidden; }
  body {
    background: var(--page-bg);
    font-family: "Open Sans", Arial, sans-serif;
    display: flex;
    align-items: center;
    justify-content: center;
    gap: 40px;
  }
  .card {
    position: relative;
    width: 560px;
    height: 320px;
    border-radius: 22px;
    overflow: hidden;
    background: linear-gradient(135deg, var(--card-white) 55%, var(--card-shade));
    box-shadow: 0 10px 28px rgba(0,0,0,0.18);
  }
  .card-shape { position: absolute; inset: 0; width: 100%; height: 100%; }

  /* Back side */
  .back-brand {
    position: absolute;
    left: 36px;
    top: 40px;
  }
  .brand-name {
    font-weight: 800;
    color: var(--brand-blue);
    letter-spacing: 0.5px;
    text-transform: uppercase;
    line-height: 1.1;
  }
  .back-brand .brand-name { font-size: 27px; }
  .back-web {
    margin-top: 6px;
    font-size: 14px;
    letter-spacing: 2px;
    color: var(--ink-grey);
  }

  /* Front side */
  .contact {
    position: absolute;
    left: 36px;
    top: 30px;
    color: var(--text-on-blue);
  }
  .contact-name {
    font-weight: 700;
    font-size: 19px;
    text-transform: uppercase;
    letter-spacing: 0.5px;
    margin-bottom: 34px;
  }
  .contact-address {
    font-size: 14px;
    line-height: 1.35;
    margin-bottom: 8px;
  }
  .contact-line {
    display: flex;
    align-items: center;
    gap: 10px;
    font-size: 14px;
    line-height: 1.6;
  }
  .contact-line svg { width: 13px; height: 13px; flex: none; }
  .front-brand {
    position: absolute;
    right: 34px;
    top: 130px;
    width: 210px;
    display: flex;
    align-items: center;
    gap: 10px;
  }
  .front-brand .brand-name { font-size: 22px; }
  .brand-dot {
    width: 16px; height: 16px; border-radius: 50%;
    background: var(--brand-blue);
    flex: none;
  }
</style>
</head>
<body>

  <section class="card card-back" aria-label="Card back">
    <div class="back-brand">
      <div class="brand-name">Meridian Capital Bridge</div>
      <div class="back-web">www.meridianbridge.co.uk</div>
    </div>
  </section>

  <section class="card card-front" aria-label="Card front">
    <svg class="card-shape" viewBox="0 0 560 320" preserveAspectRatio="none" aria-hidden="true">
      <defs>
        <linearGradient id="blueFill" x1="0" y1="0" x2="1" y2="1">
          <stop offset="0" stop-color="var(--blue-dark)"/>
          <stop offset="0.45" stop-color="var(--blue-light)"/>
          <stop offset="1" stop-color="var(--blue-dark)"/>
        </linearGradient>
      </defs>
      <path d="M0 0 H410 C320 30 262 150 298 320 H0 Z" fill="url(#blueFill)"/>
      <path d="M430 10 C335 42 282 160 318 320" fill="none" stroke="var(--accent-green)" stroke-width="6"/>
    </svg>

    <div class="contact">
      <div class="contact-name">Brett Kolvane</div>
      <div class="contact-address">
        Suite 41, R T House<br>
        Hazelbrook Lane, Watford<br>
        WD17 4QL
      </div>
      <div class="contact-line">
        <svg viewBox="0 0 24 24" fill="currentColor" aria-hidden="true"><path d="M6.6 10.8a15 15 0 0 0 6.6 6.6l2.2-2.2a1 1 0 0 1 1-.25 11.4 11.4 0 0 0 3.6.57 1 1 0 0 1 1 1V20a1 1 0 0 1-1 1A17 17 0 0 1 3 4a1 1 0 0 1 1-1h3.5a1 1 0 0 1 1 1c0 1.25.2 2.45.57 3.57a1 1 0 0 1-.25 1z"/></svg>
        <span>020 7946 0381</span>
      </div>
      <div class="contact-line">
        <svg viewBox="0 0 24 24" fill="currentColor" aria-hidden="true"><path d="M2 5h20v14H2z M2 5l10 8 10-8" stroke="#1f5fae" stroke-width="1.5"/></svg>
        <span>hello@meridianbridge.co.uk</span>
      </div>
      <div class="contact-line">
        <svg viewBox="0 0 24 24" aria-hidden="true"><circle cx="12" cy="12" r="10" fill="currentColor"/><path d="M2 12h20M12 2c3 3 3 17 0 20M12 2c-3 3-3 17 0 20" stroke="#1f5fae" stroke-width="1.5" fill="none"/></svg>
        <span>www.meridianbridge.co.uk</span>
      </div>
    </div>

    <div class="front-brand">
      <span class="brand-dot" aria-hidden="true"></span>
      <div class="brand-name">Meridian Capital Bridge</div>
    </div>
  </section>

</body>
</html>
```